Poetry Book Cover Design Project

Looking for a minimalistic book cover design for a collection of poems. The book title is "Before The Morning Turns To Glass". There are three parts to the book. First covers poetry in the theme of Rage. Second love and desire. The third is strange poems. Essentially the sections are "Rage", "Desire" and the "Strange". The reason for the title "Before The Morning Turns To Glass" is as if someone is writing these till life changes towards the intended outcome as felt in each poem. I want to have the author's name "Nirosha Kulathunge" at the bottom. Ilustration attached.
- Minimalistic

```html
<!DOCTYPE html>
<html lang="en">
<head>
<meta charset="utf-8">
<title>Before The Morning Turns To Glass — Nirosha Kulathunge</title>
<link rel="stylesheet" href="https://fonts.googleapis.com/css2?family=Cinzel:wght@400&family=Raleway:wght@400&display=swap">
<style>
  :root {
    --paper: #ffffff;
    --ink-blue: #3f6fb6;
    --line-blue-soft: #e6eef9;
    --line-blue-faint: #f4f8fd;
    --author-grey: #7a7a7a;
  }
  html, body {
    margin: 0;
    padding: 0;
    overflow: hidden;
    background: var(--paper);
  }
  .cover {
    position: relative;
    width: 847px;
    height: 1200px;
    background: var(--paper);
    overflow: hidden;
  }
  .cover__illustration {
    position: absolute;
    left: 205px;
    top: 95px;
    width: 490px;
    height: 540px;
    border-radius: 48% 52% 40% 46%;
    background: radial-gradient(ellipse at 60% 40%, var(--line-blue-soft) 0%, var(--line-blue-faint) 55%, var(--paper) 80%);
  }
  .cover__title {
    position: absolute;
    left: 428px;
    top: 420px;
    margin: 0;
    font-family: "Cinzel", "Times New Roman", serif;
    font-weight: 400;
    font-size: 54px;
    line-height: 65px;
    color: var(--ink-blue);
    text-transform: uppercase;
    letter-spacing: 0.01em;
  }
  .cover__title span {
    display: block;
  }
  .cover__author {
    position: absolute;
    left: 0;
    right: 0;
    top: 1018px;
    margin: 0;
    text-align: center;
    font-family: "Raleway", "Helvetica Neue", Arial, sans-serif;
    font-weight: 400;
    font-size: 29px;
    letter-spacing: 0.14em;
    color: var(--author-grey);
  }
</style>
</head>
<body>
  <main class="cover">
    <div class="cover__illustration" role="img" aria-label="Continuous single-line drawing in blue of a face in profile beside a leafy stem"></div>
    <h1 class="cover__title">
      <span>Before</span>
      <span>The</span>
      <span>Morning</span>
      <span>Turns</span>
      <span>To</span>
      <span>Glass</span>
    </h1>
    <p class="cover__author">Nirosha Kulathunge</p>
  </main>
</body>
</html>
```